Banner Design

A law firm looking for a logo that can be used in a web banner that highlights the web address "splitpathcounsel.net" and incorporates our law firms name- Brantley and Associates. Would prefer a design with softer green color like Russian Green.

A preliminary thought would be a boxed banner with a Brantley and Associates logo on either side of the web address "splitpathcounsel.net".

Traditional and modern designs welcomed.
Updates

   Please make sure that "splitpathcounsel.net" is the main focus of the banner.  All advertising is being done to brand that website address.  Our law firm name/logo needs to be incorporated but not the focal point.  This banner will be listed at the top of every web page.

Designers feel free to go with an over/under design with splitpathcounsel.net going on top in a prominent position over our firm name. If that style sparks your creativity.  Remember this will be the banner design that will go on top of every page of the new website.        

                                I was thinking the firm name/logo on either side of the "splitpathcounsel.net" would look balanced. But from the designs that I have received maybe it would look more balance with the "splitpathcounsel.net" illustration over the firm name.

Target Market(s)

individuals 30-50

Industry/Entity Type

Law Firm

Logo Text

Brantley and Associates splitpathcounsel.net

Logo styles of interest
Emblem Logo
Wordmark Logo

```html
<!DOCTYPE html>
<html lang="en">
<head>
<meta charset="utf-8">
<title>Brantley and Associates — splitpathcounsel.net</title>
<link rel="stylesheet" href="https://fonts.googleapis.com/css2?family=Crimson+Pro:wght@600;700&family=Roboto+Condensed:wght@700&display=swap">
<style>
  :root {
    --paper-light: #ebe7da;
    --paper-mid: #d6d1bd;
    --paper-edge: #b2ad96;
    --stone-light: #d9d6c6;
    --stone-dark: #9a9a82;
    --russian-green: #5f8a5f;
    --russian-green-deep: #4b704b;
    --ink: #433d35;
    --ink-soft: #4d473f;
    --gavel-dark: #2a2622;
    --gavel-mid: #4a423a;
  }
  html, body {
    margin: 0;
    padding: 0;
    width: 1200px;
    height: 174px;
    overflow: hidden;
  }
  .banner {
    position: relative;
    width: 1200px;
    height: 174px;
    overflow: hidden;
    background:
      linear-gradient(180deg, rgba(103, 146, 103, 0.10) 0%, rgba(103, 146, 103, 0) 60%),
      radial-gradient(ellipse 55% 120% at 52% 40%, var(--paper-light) 0%, var(--paper-mid) 60%, var(--paper-edge) 100%);
  }
  .colonnade {
    position: absolute;
    left: 0;
    top: 0;
    width: 300px;
    height: 174px;
    background: linear-gradient(90deg, var(--stone-dark) 0%, var(--stone-light) 55%, rgba(217, 214, 198, 0) 100%);
  }
  .office-address {
    position: absolute;
    top: 12px;
    right: 26px;
    margin: 0;
    font-family: "Roboto Condensed", "Arial Narrow", sans-serif;
    font-weight: 700;
    font-size: 17px;
    line-height: 20px;
    color: var(--ink-soft);
  }
  .firm-name {
    position: absolute;
    left: 286px;
    top: 52px;
    margin: 0;
    font-family: "Crimson Pro", Georgia, serif;
    font-weight: 600;
    font-size: 34px;
    line-height: 38px;
    letter-spacing: -0.8px;
    color: var(--ink);
  }
  .firm-name span { display: block; }
  .divider {
    position: absolute;
    left: 558px;
    top: 141px;
    width: 160px;
    height: 2px;
    background: var(--russian-green-deep);
  }
  .web-address {
    position: absolute;
    left: 728px;
    top: 106px;
    margin: 0;
    font-family: "Crimson Pro", Georgia, serif;
    font-weight: 700;
    font-size: 42px;
    line-height: 46px;
    letter-spacing: -0.8px;
    color: var(--russian-green-deep);
  }
  .gavel {
    position: absolute;
    left: 1098px;
    top: 78px;
    width: 84px;
    height: 86px;
    border-radius: 10px;
    background: radial-gradient(ellipse at 50% 70%, var(--gavel-mid) 0%, var(--gavel-dark) 70%, rgba(42, 38, 34, 0) 100%);
  }
</style>
</head>
<body>
  <header class="banner">
    <div class="colonnade" role="img" aria-label="Photograph of classical stone columns fading into the banner"></div>
    <p class="office-address">Office No. 123, XYZ Street, Main City</p>
    <h1 class="firm-name"><span>Brantley and</span><span>Associates</span></h1>
    <div class="divider"></div>
    <p class="web-address">splitpathcounsel.net</p>
    <div class="gavel" role="img" aria-label="Photograph of a wooden judge's gavel resting on its block"></div>
  </header>
</body>
</html>
```